Business cards to launch an education platform

Hi,
I am looking at having new business cards designed.
I am a startup, developing a web platform for schools and university, the education world. It's an online assessment system.
I would like a card that looks classy, and that is using the colors and the font of my logo.

I have attached:
1) my logo
2) A business card that I have designed quickly so you can have all the information required in the card, but I really don't like it.
3) The font that I am using (Lato Regular) to design my web platform
4) Some screenshots of my web platform so you can have a look at the style that I have.

Target Market(s)

Major market: Education system: Schools and university
Minor markets: Business in general

Industry/Entity Type

Business

Contact Information for Business Card

Tessa Vinall
Director

M: 0487 312 950
E: tessa.vinall@copperLoomVentures.com.au

Requirements
Must have
• The colors of my logo

```html
<!DOCTYPE html>
<html lang="en">
<head>
<meta charset="utf-8">
<title>Copper Loom Ventures – Business Cards</title>
<link rel="stylesheet" href="https://fonts.googleapis.com/css2?family=Lato:wght@400;700&display=swap">
<style>
  :root {
    --backdrop: #e9eaec;
    --paper: #ffffff;
    --navy: #0b3f7a;
    --blue-deep: #0a4f9e;
    --blue-mid: #0d63bf;
    --blue-bright: #1677d2;
    --cyan: #22b7e8;
    --text-light: #ffffff;
  }
  * { box-sizing: border-box; margin: 0; padding: 0; }
  html, body {
    width: 1105px;
    height: 1200px;
    overflow: hidden;
    background: var(--backdrop);
    font-family: "Lato", sans-serif;
  }
  .sheet {
    position: relative;
    width: 1105px;
    height: 1200px;
  }
  .card {
    position: absolute;
    left: 179px;
    width: 747px;
    height: 428px;
    overflow: hidden;
  }
  .card--front { top: 119px; background: var(--paper); }
  .card--back { top: 638px; }

  /* Front */
  .brand-lockup {
    position: absolute;
    top: 108px;
    left: 0;
    width: 100%;
    display: flex;
    align-items: center;
    justify-content: center;
    gap: 18px;
  }
  .brand-lockup__square {
    width: 54px;
    height: 54px;
    background: var(--blue-mid);
  }
  .brand-lockup__name {
    color: var(--navy);
    font-size: 40px;
    font-weight: 400;
    letter-spacing: 2px;
  }
  .front-band {
    position: absolute;
    left: 0;
    top: 250px;
    width: 747px;
    height: 178px;
  }
  .contact {
    position: absolute;
    left: 42px;
    top: 324px;
    color: var(--text-light);
    font-size: 20px;
    line-height: 33px;
  }
  .contact__row { display: flex; align-items: center; gap: 14px; }
  .contact__icon { width: 16px; height: 18px; flex: none; }
  .holder {
    position: absolute;
    right: 40px;
    top: 308px;
    text-align: center;
    color: var(--text-light);
  }
  .holder__name { font-size: 29px; letter-spacing: -0.5px; }
  .holder__role { font-size: 24px; margin-top: 2px; }

  /* Back */
  .back-field {
    position: absolute;
    inset: 0;
    background:
      radial-gradient(ellipse 60% 70% at 78% 78%, rgba(34,183,232,0.55), transparent 70%),
      linear-gradient(125deg, var(--blue-deep) 0%, var(--blue-mid) 55%, var(--blue-bright) 100%);
  }
  .back-brand {
    position: absolute;
    top: 135px;
    left: 0;
    width: 100%;
    padding-left: 90px;
    text-align: center;
    color: var(--text-light);
  }
  .back-brand__name {
    font-size: 58px;
    font-weight: 400;
    letter-spacing: 5px;
    line-height: 1.15;
  }
  .back-brand__url {
    font-size: 21px;
    letter-spacing: 1px;
    margin-top: 14px;
  }
</style>
</head>
<body>
<main class="sheet">

  <section class="card card--front" aria-label="Business card front">
    <div class="brand-lockup">
      <span class="brand-lockup__square" aria-hidden="true"></span>
      <span class="brand-lockup__name">Copper Loom Ventures</span>
    </div>

    <svg class="front-band" viewBox="0 0 747 178" preserveAspectRatio="none" aria-hidden="true">
      <defs>
        <radialGradient id="bandGlow" cx="0.55" cy="0.55" r="0.65">
          <stop offset="0" stop-color="#1677d2"/>
          <stop offset="1" stop-color="#0a4a96"/>
        </radialGradient>
      </defs>
      <polyline points="0,3 623,3 644,25 665,3 747,3" fill="none" stroke="#22b7e8" stroke-width="5"/>
      <polygon points="0,12 619,12 644,37 669,12 747,12 747,178 0,178" fill="url(#bandGlow)"/>
    </svg>

    <div class="contact">
      <div class="contact__row">
        <svg class="contact__icon" viewBox="0 0 16 18" aria-hidden="true">
          <rect x="3" y="0.5" width="10" height="17" rx="1.5" fill="none" stroke="#fff" stroke-width="1.6"/>
          <rect x="5" y="3" width="6" height="10" fill="#fff"/>
        </svg>
        <span>0487 312 950</span>
      </div>
      <div class="contact__row">
        <svg class="contact__icon" viewBox="0 0 16 18" aria-hidden="true">
          <rect x="0.5" y="4" width="15" height="10" fill="#fff"/>
          <polyline points="0.5,4 8,10 15.5,4" fill="none" stroke="#0a4f9e" stroke-width="1.3"/>
        </svg>
        <span>tessa.vinall@copperLoomVentures.com.au</span>
      </div>
    </div>

    <div class="holder">
      <p class="holder__name">Tessa Vinall</p>
      <p class="holder__role">Director</p>
    </div>
  </section>

  <section class="card card--back" aria-label="Business card back">
    <div class="back-field" role="img" aria-label="Large faint brand mark in blue tones"></div>
    <div class="back-brand">
      <p class="back-brand__name">Copper Loom Ventures</p>
      <p class="back-brand__url">www.copperLoomVentures.com.au</p>
    </div>
  </section>

</main>
</body>
</html>
```